HARBORLINE AUTO GLASS

Mobile Glass Shop:

1) Windshield REPAIR 2)Windshield replacment 3) Rear Windshield Replacment 4) Side Window Replacment 5) car window replacment 6) Power Window Repair.

Schedual a service within 24 hour with one of our certified technicians.

See "clearvane auto repair" web site for referance on the nature of our buisness and service. www.clearvane-example.com

```html
<!DOCTYPE html>
<html lang="en">
<head>
<meta charset="utf-8">
<title>Harborline Auto Glass</title>
<link href="https://fonts.googleapis.com/css2?family=Jost:wght@400;500;600;700&family=Arimo:wght@400;700&display=swap" rel="stylesheet">
<style>
:root{
  --sky:#00a0d8;
  --navy-btn:#0a5d9a;
  --ink:#4a4a4a;
  --dark:#1f2d3d;
  --text:#555;
  --footer:#0d2b45;
  --footer-text:#b9c6d3;
  --white:#fff;
}
*{margin:0;padding:0;box-sizing:border-box}
html,body{width:1200px;height:2906px;overflow:hidden}
body{position:relative;font-family:Arimo,Arial,sans-serif;color:var(--text);background:var(--white)}
.abs{position:absolute}
.heading{font-family:Jost,sans-serif}
.btn{position:absolute;background:var(--navy-btn);color:var(--white);font-size:13px;display:flex;align-items:center;justify-content:center;border-radius:2px}

.topbar{left:0;top:0;width:1200px;height:28px;background:var(--sky);color:var(--white);font-size:12px;text-align:center;line-height:28px}
.header{left:0;top:28px;width:1200px;height:72px;background:var(--white)}
.logo-box{left:121px;top:28px;width:162px;height:94px;background:var(--white);box-shadow:0 4px 12px rgba(0,0,0,.12);z-index:3;display:flex;flex-direction:column;justify-content:center;padding-left:18px}
.logo-name{font-family:Jost,sans-serif;font-weight:700;font-size:18px;color:var(--navy-btn);line-height:1.05}
.nav a{position:absolute;top:56px;font-size:13px;color:#444;text-decoration:none}

.hero{left:0;top:100px;width:1200px;height:526px;background:linear-gradient(90deg,#f4f6f8 0%,#eef1f4 38%,#b9c1c8 55%,#6d7379 75%,#3a3d42 100%)}
.hero-title{left:152px;top:238px;font-family:Jost,sans-serif;font-weight:700;font-size:54px;color:var(--sky);letter-spacing:1px}
.hero-sub{left:152px;top:297px;font-family:Jost,sans-serif;font-weight:700;font-size:33px;color:var(--ink);letter-spacing:1px}
.hero-copy{left:152px;top:358px;width:370px;font-size:13.5px;line-height:22px;color:#555}

.photo{position:absolute;box-shadow:0 6px 16px rgba(0,0,0,.18)}
.eyebrow{font-size:13px;letter-spacing:1.5px;color:var(--sky)}
.eyebrow::before{content:"";display:inline-block;width:37px;height:1px;background:var(--sky);vertical-align:middle;margin-right:12px}
.about-title{left:711px;top:814px;font-family:Jost,sans-serif;font-weight:600;font-size:33px;color:var(--ink)}
.about-title span,.cta-title span{color:var(--sky)}
.about-copy{left:711px;width:330px;font-size:12px;line-height:20.5px;color:#555}

.services{left:0;top:1230px;width:1200px;height:960px;background:var(--sky)}
.services-title{left:0;width:1200px;top:1306px;text-align:center;font-family:Jost,sans-serif;font-weight:600;font-size:40px;color:var(--white)}
.card{position:absolute;width:273px;height:354px;background:var(--white);padding:4px}
.card-img{position:relative;width:265px;height:200px;overflow:hidden}
.card-img svg{position:absolute;left:0;bottom:0}
.card h3{font-family:Jost,sans-serif;font-weight:500;font-size:16px;color:var(--dark);margin:16px 0 0 17px;line-height:19px;text-transform:uppercase}
.card p{font-size:11px;line-height:20px;color:#444;margin:8px 16px 0 17px;height:60px}
.card .more{position:absolute;left:22px;bottom:22px;font-size:11px;color:var(--sky)}

.cta-title{left:0;width:1200px;top:2258px;text-align:center;font-family:Jost,sans-serif;font-weight:600;font-size:34px;line-height:42px;color:var(--ink)}

.help{left:349px;top:2482px;width:503px;height:67px;background:var(--sky);color:var(--white);z-index:2;display:flex;align-items:center}
.footer{left:0;top:2510px;width:1200px;height:396px;background:var(--footer)}
.f-title{font-family:Jost,sans-serif;font-size:15px;color:var(--white)}
.f-title::after{content:"";display:block;width:22px;height:2px;background:var(--sky);margin-top:6px}
.f-list{list-style:none;font-size:11px;color:var(--footer-text);line-height:25px}
.f-text{font-size:11px;color:var(--footer-text);line-height:18px}
.vline{position:absolute;top:2608px;width:1px;height:150px;background:rgba(255,255,255,.12)}
.social{position:absolute;top:2736px;width:29px;height:29px;border-radius:50%}
</style>
</head>
<body>

<div class="abs topbar">Schedual a service within 24 hour with one of our certified technicians.</div>
<div class="abs header"></div>
<div class="abs logo-box"><div class="logo-name">HARBORLINE<br>AUTO GLASS</div></div>
<nav class="nav">
  <a style="left:557px">Home</a>
  <a style="left:626px">Services</a>
  <a style="left:707px">About</a>
  <a style="left:776px">Location</a>
  <a style="left:857px">Contact</a>
</nav>
<div class="btn" style="left:925px;top:48px;width:154px;height:33px;font-size:12px">Schedule a Consultation</div>

<section class="abs hero" role="img" aria-label="Smiling technician giving a thumbs up while fitting a windshield with suction tools"></section>
<h1 class="abs hero-title">FIX THAT BREAK</h1>
<h2 class="abs hero-sub">WITHOUT GOING BROKE</h2>
<p class="abs hero-copy">Lorem ipsum dolor sit amet, consectetur adipisicing elit, sed do eiusmod tempor incididunt ut labore et dolore.</p>
<div class="btn" style="left:152px;top:434px;width:186px;height:37px">Schedule a Consultation</div>

<div class="photo" style="left:169px;top:700px;width:255px;height:339px;background:linear-gradient(160deg,#7c8b99,#3a3f4a 60%,#2a2430)" role="img" aria-label="Technician applying sealant to a windshield edge"></div>
<div class="photo" style="left:436px;top:760px;width:226px;height:163px;background:linear-gradient(160deg,#8a9a6a,#c9cfd4 55%,#3b4046)" role="img" aria-label="Windshield being lifted onto a car outdoors"></div>
<div class="photo" style="left:436px;top:935px;width:176px;height:212px;background:linear-gradient(160deg,#4f6a3c,#2a3a30 50%,#7a8b7e)" role="img" aria-label="Gloved hands using a tool on windshield glass"></div>

<div class="abs eyebrow" style="left:711px;top:791px">WELCOME TO</div>
<h2 class="abs about-title">Harborline <span>Auto Glass</span></h2>
<p class="abs about-copy" style="top:872px">Lorem ipsum dolor sit amet, consectetur adipisicing elit, sed do eiusmod tempor incididunt ut labore et dolore magna aliqua ut enim ad minim.</p>
<p class="abs about-copy" style="top:954px">Quis nostrud exercitation ullamco laboris nisi ut aliquip ex ea commodo consequat, Duis aute irure dolor in reprehenderit in voluptate velit esse cillum dolore eu fugiat nulla pariatur.</p>
<div class="btn" style="left:711px;top:1070px;width:120px;height:38px;font-size:11px;font-weight:700">LEARN MORE</div>

<section class="abs services"></section>
<div class="abs eyebrow" style="left:0;width:1200px;top:1289px;text-align:center;color:var(--white)"><span style="display:inline-block">AUTO GLASS</span></div>
<h2 class="abs services-title">Our Services</h2>

<!-- row 1 -->
<div class="card" style="left:179px;top:1398px">
  <div class="card-img" role="img" aria-label="Windshield chip repair tool on glass" style="background:linear-gradient(160deg,#9aa3ab,#4a5460)">
    <svg width="265" height="60" viewBox="0 0 265 60"><polygon points="0,60 80,12 265,48 265,60" fill="#0a5d9a"/><polygon points="0,60 80,18 265,54 265,60" fill="#fff"/></svg>
  </div>
  <h3>Windshield Repair</h3>
  <p>Lorem ipsum dolor sit amet, consectetur adipisicing elit, sed do eiusmod tempor incididunt ut labore et dolore magna...</p>
  <div class="more">Learn More &nbsp;⟶</div>
</div>
<div class="card" style="left:465px;top:1398px">
  <div class="card-img" role="img" aria-label="Two technicians fitting a new windshield" style="background:linear-gradient(160deg,#c4c9cd,#5b6570)">
    <svg width="265" height="60" viewBox="0 0 265 60"><polygon points="0,60 80,12 265,48 265,60" fill="#0a5d9a"/><polygon points="0,60 80,18 265,54 265,60" fill="#fff"/></svg>
  </div>
  <h3>Windshield Replacment</h3>
  <p>Lorem ipsum dolor sit amet, consectetur adipisicing elit, sed do eiusmod tempor incididunt ut labore et dolore magna...</p>
  <div class="more">Learn More &nbsp;⟶</div>
</div>
<div class="card" style="left:749px;top:1398px">
  <div class="card-img" role="img" aria-label="Shattered rear windshield" style="background:linear-gradient(160deg,#b0bcc6,#3d4a57)">
    <svg width="265" height="60" viewBox="0 0 265 60"><polygon points="0,60 80,12 265,48 265,60" fill="#0a5d9a"/><polygon points="0,60 80,18 265,54 265,60" fill="#fff"/></svg>
  </div>
  <h3>Rear Windshield<br>Replacment</h3>
  <p style="height:40px">Lorem ipsum dolor sit amet, consectetur adipisicing elit, sed do eiusmod tempor</p>
  <div class="more">Learn More &nbsp;⟶</div>
</div>

<!-- row 2 -->
<div class="card" style="left:179px;top:1763px">
  <div class="card-img" role="img" aria-label="Broken side window seen from the driver seat" style="background:linear-gradient(160deg,#6f7880,#2b3036)">
    <svg width="265" height="60" viewBox="0 0 265 60"><polygon points="0,60 80,12 265,48 265,60" fill="#0a5d9a"/><polygon points="0,60 80,18 265,54 265,60" fill="#fff"/></svg>
  </div>
  <h3>Side Window Replacment</h3>
  <p>Lorem ipsum dolor sit amet, consectetur adipisicing elit, sed do eiusmod tempor incididunt ut labore et dolore magna...</p>
  <div class="more">Learn More &nbsp;⟶</div>
</div>
<div class="card" style="left:465px;top:1763px">
  <div class="card-img" role="img" aria-label="Technician replacing a car window in a workshop" style="background:linear-gradient(160deg,#9a9ea3,#2f3237 60%,#c9782e)">
    <svg width="265" height="60" viewBox="0 0 265 60"><polygon points="0,60 80,12 265,48 265,60" fill="#0a5d9a"/><polygon points="0,60 80,18 265,54 265,60" fill="#fff"/></svg>
  </div>
  <h3>Car Window Replacment</h3>
  <p>Lorem ipsum dolor sit amet, consectetur adipisicing elit, sed do eiusmod tempor incididunt ut labore et dolore magna...</p>
  <div class="more">Learn More &nbsp;⟶</div>
</div>
<div class="card" style="left:749px;top:1763px">
  <div class="card-img" role="img" aria-label="Hands repairing a power window mechanism inside a door" style="background:linear-gradient(160deg,#a9adb1,#5e6369)">
    <svg width="265" height="60" viewBox="0 0 265 60"><polygon points="0,60 80,12 265,48 265,60" fill="#0a5d9a"/><polygon points="0,60 80,18 265,54 265,60" fill="#fff"/></svg>
  </div>
  <h3>Power Window Repair.</h3>
  <p>Lorem ipsum dolor sit amet, consectetur adipisicing elit, sed do eiusmod tempor incididunt ut labore et dolore magna...</p>
  <div class="more">Learn More &nbsp;⟶</div>
</div>

<h2 class="abs cta-title">Don't Wait, Schedule <span>Your</span><br><span>Appointment Today!</span></h2>
<div class="btn" style="left:508px;top:2367px;width:185px;height:37px">Get quote + schedule</div>

<section class="abs footer"></section>
<div class="abs help">
  <span style="font-size:24px;margin-left:21px">Need help:</span>
  <svg style="margin-left:44px" width="36" height="36" viewBox="0 0 24 24" fill="none" stroke="#fff" stroke-width="1.8"><path d="M5 3h4l2 5-2.5 1.5a11 11 0 0 0 6 6L16 13l5 2v4a2 2 0 0 1-2 2A16 16 0 0 1 3 5a2 2 0 0 1 2-2z"/><path d="M15 3a6 6 0 0 1 6 6M15 7a2 2 0 0 1 2 2"/></svg>
  <span class="heading" style="font-size:33px;font-weight:700;margin-left:14px;letter-spacing:1px">08 40 55 21 90</span>
</div>

<div class="abs logo-name" style="left:113px;top:2602px;color:var(--white);font-size:20px">HARBORLINE<br>AUTO GLASS</div>
<p class="abs f-text" style="left:113px;top:2676px;width:190px">Consectetur adipisicing elit, sed do eiusmod tempor incididunt.</p>
<p class="abs f-text" style="left:112px;top:2731px">Phone: 08 40 55 21 90</p>
<p class="abs f-text" style="left:112px;top:2763px">Email: info@harborlineglass.example</p>

<div class="vline" style="left:352px"></div>
<div class="vline" style="left:550px"></div>
<div class="vline" style="left:776px"></div>

<div class="abs f-title" style="left:387px;top:2606px">Quick Link</div>
<ul class="abs f-list" style="left:387px;top:2640px">
  <li>Home</li><li>Service</li><li>About</li><li>Location</li><li>Contact</li><li>Schedule A Consultation</li>
</ul>
<div class="abs f-title" style="left:585px;top:2606px">Important Link</div>
<ul class="abs f-list" style="left:585px;top:2640px">
  <li>Windshield Repair</li><li>Windshield Replacement</li><li>Rear Windshield Replacement</li><li>Side Window Replacement</li><li>Car Window Replacement</li><li>Power Window Repair</li>
</ul>
<div class="abs f-title" style="left:809px;top:2606px">Subscribe to Our Newsletter</div>
<div class="abs" style="left:809px;top:2642px;width:200px;height:31px;border:1px solid rgba(255,255,255,.2);font-size:12px;color:var(--footer-text);padding:8px 10px">Email</div>
<div class="abs" style="left:1009px;top:2642px;width:82px;height:31px;background:var(--sky);color:#fff;font-size:11px;font-weight:700;text-align:center;line-height:31px">SUBSCRIBE</div>
<p class="abs f-text" style="left:809px;top:2686px;width:280px">Lorem ipsum dolor sit amet, consectetur adipisicing elit, sed do eiusmod tempor incididunt.</p>
<div class="social" style="left:809px;background:#2c4660"></div>
<div class="social" style="left:848px;background:var(--sky)"></div>
<div class="social" style="left:887px;background:#2c4660"></div>

<div class="abs" style="left:112px;top:2854px;width:1010px;height:1px;background:rgba(255,255,255,.12)"></div>
<p class="abs" style="left:0;width:1200px;top:2872px;text-align:center;font-size:12px;color:var(--white)">Copyright © 2022 <span style="color:var(--sky)">Harborline Auto Glass</span>. All rights reserved.</p>

</body>
</html>
```